Residential Roofing Company, need a Unique business card for a Woman owned ompany

Woman Owned Residential Roofing Company. Specializing in Insurance Claims
Attention to Detail is what sets this woman owned roofing company apart from the rest
We are TRV Certified and are an Accredited business with an A rating with the QPL. Our Contractor License number KMT48395

```html
<!DOCTYPE html>
<html lang="en">
<head>
<meta charset="UTF-8">
<meta name="description" content="Crestline Roofing – woman-owned residential roofing company specializing in insurance claims. TRV Certified, QPL Accredited (A rating), Contractor License KMT48395.">
<title>Crestline Roofing – Woman-Owned Residential Roofing, Insurance Claims Specialists</title>
<link href="https://fonts.googleapis.com/css2?family=Lato:wght@400;700&family=Open+Sans:wght@700;800&display=swap" rel="stylesheet">
<style>
  :root {
    --backdrop: #a3a3a3;
    --navy: #0b2c6b;
    --navy-deep: #010610;
    --navy-mid: #03183d;
    --ink: #1d1d1d;
    --rule: #9a9a9a;
    --white: #ffffff;
    --badge-blue: #0a6aa1;
    --badge-red: #e0202a;
    --badge-grey: #8f8f8f;
  }
  * { margin: 0; padding: 0; box-sizing: border-box; }
  html, body {
    width: 1200px; height: 1200px; overflow: hidden;
    background: var(--backdrop);
  }
  .card {
    position: absolute;
    top: 303px;
    height: 594px;
    overflow: hidden;
  }
  .card-front {
    left: 200px; width: 370px;
    background: linear-gradient(200deg, var(--navy-deep) 0%, var(--navy-mid) 40%, var(--navy) 100%);
  }
  .card-back {
    left: 599px; width: 364px;
    background: var(--white);
  }
  .wordmark {
    position: absolute; left: 0; right: 0;
    text-align: center;
    font-family: "Open Sans", sans-serif;
    font-weight: 800;
    font-size: 27px;
    letter-spacing: -0.5px;
    line-height: 1;
  }
  .card-front .wordmark { top: 445px; color: var(--white); }
  .card-back .wordmark { top: 155px; color: var(--navy); }
  .license {
    position: absolute; left: 0; right: 0; top: 530px;
    text-align: center;
    font-family: "Lato", sans-serif;
    font-size: 20px;
    color: var(--white);
  }
  .person-name {
    position: absolute; left: 0; right: 0; top: 271px;
    text-align: center;
    font-family: "Open Sans", sans-serif;
    font-weight: 700;
    font-size: 25px;
    color: var(--navy);
    line-height: 1;
  }
  .person-role {
    position: absolute; left: 0; right: 0; top: 299px;
    text-align: center;
    font-family: "Lato", sans-serif;
    font-size: 17px;
    color: var(--ink);
  }
  .icon-row {
    position: absolute; left: 87px; right: 87px; top: 331px;
    display: flex; align-items: center; gap: 4px;
  }
  .icon-row .rule { flex: 1; height: 1px; background: var(--rule); }
  .icon-row .icon {
    width: 25px; height: 25px; border-radius: 3px;
    background: var(--navy);
    display: flex; align-items: center; justify-content: center;
  }
  .contact-list, .address {
    position: absolute; left: 0; right: 0;
    text-align: center;
    font-family: "Lato", sans-serif;
    font-size: 17.5px;
    line-height: 21.7px;
    color: var(--ink);
  }
  .contact-list { top: 367px; }
  .contact-list .accent { color: var(--navy); }
  .address { top: 453px; }
  .divider {
    position: absolute; left: 88px; right: 80px; height: 1px;
    background: var(--rule);
  }
  .divider-top { top: 442px; }
  .divider-bottom { top: 507px; }
  .badge { position: absolute; display: block; }
  .badge-accredited { left: 62px; top: 528px; width: 103px; height: 40px; }
  .badge-certified { left: 186px; top: 523px; width: 116px; height: 45px; }
</style>
</head>
<body>
  <section class="card card-front" aria-label="Crestline Roofing, woman-owned residential roofing, insurance claims specialists">
    <div class="wordmark">CRESTLINE ROOFING</div>
    <p class="license">License Number KMT48395</p>
  </section>

  <section class="card card-back" aria-label="Contact card, Crestline Roofing, woman-owned, TRV Certified and QPL Accredited">
    <div class="wordmark">CRESTLINE ROOFING</div>

    <h1 class="person-name">DANIEL HARTLEY</h1>
    <p class="person-role">Managing Director</p>

    <div class="icon-row">
      <span class="rule"></span>
      <span class="icon" aria-label="Phone">
        <svg width="15" height="15" viewBox="0 0 16 16"><path d="M2 5c0-2 3-3 6-3s6 1 6 3v1h-3V5H5v1H2z M4 8h8l1 5H3z" fill="#fff"/></svg>
      </span>
      <span class="icon" aria-label="Email">
        <svg width="15" height="15" viewBox="0 0 16 16"><rect x="1.5" y="3.5" width="13" height="9" fill="none" stroke="#fff" stroke-width="1.2"/><path d="M1.5 3.5 8 9l6.5-5.5M1.5 12.5 6 7.5M14.5 12.5 10 7.5" fill="none" stroke="#fff" stroke-width="1.2"/></svg>
      </span>
      <span class="icon" aria-label="Website">
        <svg width="15" height="15" viewBox="0 0 16 16"><circle cx="8" cy="8" r="6.5" fill="#fff"/><path d="M5 4c2 0 3 2 2 3s-3 1-2 3M10 9c1 0 2 1 1 3" fill="none" stroke="#0b2c6b" stroke-width="1.4"/></svg>
      </span>
      <span class="rule"></span>
    </div>

    <p class="contact-list">
      044-987 654 321<br>
      hello@crestmail.com<br>
      www.<span class="accent">crestlineroof</span>.com
    </p>
    <div class="divider divider-top"></div>
    <p class="address">
      87, Harbor Lane<br>
      30918, Eastland
    </p>
    <div class="divider divider-bottom"></div>

    <svg class="badge badge-accredited" viewBox="0 0 103 40" role="img" aria-label="QPL Accredited Business badge, A rating">
      <rect x="0.5" y="0.5" width="102" height="39" rx="5" fill="var(--badge-blue)" stroke="var(--badge-blue)"/>
      <rect x="3" y="3" width="28" height="34" rx="3" fill="#fff"/>
    </svg>
    <svg class="badge badge-certified" viewBox="0 0 116 45" role="img" aria-label="TRV Certified roofing contractor badge">
      <rect x="0" y="6" width="116" height="3" fill="var(--badge-grey)"/>
      <rect x="0" y="9" width="116" height="31" fill="var(--badge-red)"/>
      <rect x="0" y="40" width="116" height="3" fill="var(--badge-grey)"/>
    </svg>
  </section>
</body>
</html>
```